Prestige Car Bodyshop Business Card

We are a car bodyshop based in the UK. Our customer base is mainly prestige high-value vehicles. I am looking for a classy and stylish business card design for my staff to give out to customers, with their direct email and phone number, as well as our main email and phone number with address details

I am also looking to have a general business card design with just our main company address and contact details, but also have a space to add a manufacturer approval logo (i.e Velmora, Orek, Tovalo etc... logo) in the corner somewhere.

I do not particularly want any outlines or pictures of cars on the card, I would just like a quality high-end look.

Please feel free to get in touch if you have any questions or queries?

Many Thanks

Malcolm

Target Market(s)

Prestige vehicle owners

Industry/Entity Type

Automotive

Contact Information for Business Card

I am looking for a classy and stylish business card design for my staff to give out to customers, with their direct email and phone number, as well as our main email and phone number with address details

Font styles to use
Sans Serif

Colors

Designer to choose colors to be used in the design.

Requirements
Nice to have
• I do not particularly want any outlines or pictures of cars on the card, I would just like a quality high-end look.

```html
<!DOCTYPE html>
<html lang="en">
<head>
<meta charset="utf-8">
<title>Harwell Accident Repair Centre – Business Cards</title>
<link rel="stylesheet" href="https://fonts.googleapis.com/css2?family=Montserrat:wght@300;400;500&display=swap">
<style>
  :root {
    --page: #eceeed;
    --card: #ffffff;
    --shade: #e4e4e4;
    --navy: #1f3f7a;
    --blue: #1b5aa6;
    --bright: #2170c4;
    --orange: #f0821e;
    --grey: #b9b9b9;
    --ink-light: #ffffff;
  }
  * { box-sizing: border-box; margin: 0; padding: 0; }
  html, body { width: 1200px; height: 900px; overflow: hidden; }
  body {
    background: var(--page);
    font-family: "Montserrat", Arial, sans-serif;
    position: relative;
  }
  .card {
    position: absolute;
    left: 320px;
    width: 560px;
    height: 320px;
    background: var(--card);
    overflow: hidden;
    box-shadow: 0 6px 18px rgba(0,0,0,.12);
  }
  .card--front { top: 110px; }
  .card--back { top: 480px; }
  .card__shade {
    position: absolute;
    inset: 0;
    background: linear-gradient(200deg, var(--shade) 0%, #f4f4f4 35%, var(--card) 55%);
    clip-path: polygon(38% 0, 100% 0, 100% 100%, 38% 0);
  }
  .card--front .card__shade { clip-path: polygon(0 0, 100% 0, 100% 38%, 0 38%); background: linear-gradient(90deg, var(--card) 35%, #f1f1f1 60%, var(--shade) 100%); }
  .card--back .card__shade { clip-path: polygon(40% 0, 100% 0, 100% 45%, 40% 45%); background: linear-gradient(90deg, #f6f6f6, var(--shade)); }

  .brand { position: absolute; display: flex; align-items: center; gap: 14px; }
  .brand__disc { width: 72px; height: 72px; border-radius: 50%; background: var(--blue); flex: none; }
  .brand__name {
    font-weight: 300; color: var(--navy); font-size: 38px; letter-spacing: 1px; line-height: 1;
    padding-bottom: 6px; border-bottom: 1px solid var(--navy);
  }
  .brand__tag { font-weight: 300; color: var(--navy); font-size: 11px; letter-spacing: 1px; margin-top: 5px; }
  .card--front .brand { left: 190px; top: 112px; }
  .card--back .brand { left: 60px; top: 190px; }
  .card--back .brand__disc { width: 62px; height: 62px; }
  .card--back .brand__name { font-size: 32px; }

  .makers { position: absolute; right: 40px; top: 210px; display: flex; gap: 26px; }
  .makers__item { font-weight: 300; color: var(--grey); font-size: 15px; letter-spacing: 1px; }

  .accent { position: absolute; left: 36px; bottom: 0; display: flex; gap: 4px; }
  .accent__block { width: 36px; height: 26px; background: var(--orange); }

  .person { position: absolute; right: 30px; top: 26px; width: 270px; }
  .person__name { font-weight: 500; color: var(--navy); font-size: 18px; letter-spacing: 2px; }
  .person__role { font-weight: 300; color: var(--navy); font-size: 10px; letter-spacing: 1px; text-align: right; padding-bottom: 6px; border-bottom: 1px solid var(--grey); margin-bottom: 10px; }
  .contact { list-style: none; }
  .contact__row {
    display: flex; justify-content: space-between; align-items: center;
    color: var(--ink-light); font-size: 11px; font-weight: 400; letter-spacing: .5px;
    padding: 8px 12px; margin-bottom: 5px; border-radius: 3px;
  }
  .contact__row--phone { background: var(--navy); line-height: 1.4; }
  .contact__row--mail { background: var(--blue); }
  .contact__row--web { background: var(--bright); }
  .contact__icon { width: 16px; height: 16px; flex: none; }
</style>
</head>
<body>

<section class="card card--front" aria-label="Card front">
  <div class="card__shade"></div>
  <div class="brand">
    <span class="brand__disc"></span>
    <div>
      <div class="brand__name">HARWELL</div>
      <div class="brand__tag">ACCIDENT REPAIR CENTRE</div>
    </div>
  </div>
  <div class="makers" aria-label="Manufacturer approvals">
    <span class="makers__item">Tovalo</span>
    <span class="makers__item">Velmora</span>
    <span class="makers__item">Orek</span>
  </div>
  <div class="accent">
    <span class="accent__block"></span><span class="accent__block"></span><span class="accent__block"></span>
  </div>
</section>

<section class="card card--back" aria-label="Card back">
  <div class="card__shade"></div>
  <div class="person">
    <div class="person__name">Malcolm Malcolm</div>
    <div class="person__role">founder and CEO</div>
    <ul class="contact">
      <li class="contact__row contact__row--phone">
        <span>01632 960 418<br>01632 960 733</span>
        <svg class="contact__icon" viewBox="0 0 16 16"><circle cx="8" cy="8" r="8" fill="#fff" opacity=".9"/><rect x="5.5" y="3.5" width="5" height="9" rx="1" fill="#1f3f7a"/></svg>
      </li>
      <li class="contact__row contact__row--mail">
        <span>info@harwellrepair.co.uk</span>
        <svg class="contact__icon" viewBox="0 0 16 16"><circle cx="8" cy="8" r="8" fill="#fff" opacity=".9"/><rect x="4" y="5" width="8" height="6" fill="#1b5aa6"/><path d="M4 5l4 3.5L12 5" stroke="#fff" stroke-width=".8" fill="none"/></svg>
      </li>
      <li class="contact__row contact__row--web">
        <span>harwellrepair.co.uk</span>
        <svg class="contact__icon" viewBox="0 0 16 16"><circle cx="8" cy="8" r="8" fill="#fff" opacity=".9"/><circle cx="8" cy="8" r="4" fill="none" stroke="#2170c4" stroke-width="1"/><path d="M4 8h8M8 4v8" stroke="#2170c4" stroke-width=".8"/></svg>
      </li>
    </ul>
  </div>
  <div class="brand">
    <span class="brand__disc"></span>
    <div>
      <div class="brand__name">HARWELL</div>
      <div class="brand__tag">ACCIDENT REPAIR CENTRE</div>
    </div>
  </div>
</section>

</body>
</html>
```